Wine Label Marabel Faye Rose or Pinot Noir

Need label design for "Marabel Faye" wine brand.
Rose or Pinot Noir.
Thinking something pretty, floral, southern inspired.

Target Market(s)

Female- age 45-65

Font styles to use
Script

Colors
eea4c8
d2a4cc
f68e4d
fee18a

```html
<!DOCTYPE html>
<html lang="en">
<head>
<meta charset="UTF-8">
<title>Marabel Faye — Wine Label</title>
<link href="https://fonts.googleapis.com/css2?family=Mrs+Saint+Delafield&family=Poiret+One&display=swap" rel="stylesheet">
<style>
  :root {
    --paper: #ffffff;
    --ink: #111111;
    --bloom: #e67b8c;
    --bloom-soft: #f2a9b3;
    --stem: #a3a37c;
    --stem-deep: #7e7f5c;
  }
  * { margin: 0; padding: 0; box-sizing: border-box; }
  html, body {
    width: 1200px;
    height: 1200px;
    overflow: hidden;
    background: var(--paper);
  }
  .label {
    position: relative;
    width: 1200px;
    height: 1200px;
    background: var(--paper);
  }
  .flower-illustration {
    position: absolute;
    left: 488px;
    top: 236px;
    width: 264px;
    height: 516px;
    border-radius: 130px 130px 40px 40px;
    background: linear-gradient(180deg,
      var(--bloom-soft) 0%,
      var(--bloom) 22%,
      var(--bloom-soft) 34%,
      var(--stem) 48%,
      var(--stem-deep) 100%);
    opacity: 0.85;
  }
  .brand-name {
    position: absolute;
    left: 0;
    top: 650px;
    width: 1200px;
    text-align: center;
    font-family: "Mrs Saint Delafield", cursive;
    font-size: 190px;
    font-weight: 400;
    line-height: 1;
    color: var(--ink);
  }
  .wine-details {
    position: absolute;
    left: 0;
    top: 893px;
    width: 1200px;
    text-align: center;
    font-family: "Poiret One", sans-serif;
    font-size: 33px;
    line-height: 39px;
    color: var(--ink);
  }
</style>
</head>
<body>
  <main class="label">
    <div class="flower-illustration" role="img" aria-label="Watercolour pink ranunculus flower on a long sage-green stem with a closed bud"></div>
    <h1 class="brand-name">Marabel Faye</h1>
    <p class="wine-details">Rose Wine or Pinot Noir<br>California, 2018</p>
  </main>
</body>
</html>
```